Anzeigengestaltung für Bernstein Ankaufstage in Wien
Zielgruppe
Zweck dieser Anzeige ist:
sowiele Leute wie möglich zu überzeugen, mit Ihrem Bernstein, zu uns in die Ankaufsaktion zu kommen.
Wer wir sind:
Wir sind eine Firma aus Deutschland, die sich auf die Bewertung und den Ankauf von Bernstein (Rohbernstein, Bernsteinschmuck, Kunstobjekte aus Bernstein etc. ) spezialisiert hat.
Wir führen in verschiedenen Städten Aktionen durch, in denen wir Bernstein bewerten und ggf. auch ankaufen.
Zielgruppe:
Alle leser einer Tageszeitung, Alter 50 + überwiegend ältere Damen, und generel Haushalte die Bernstein besitzen
siehe Bsp. Anzeige Wien (Datei upload)
Aufgabenstellung
Anzeigengröße B 198 mm x H 270 mm
Technische Angaben siehe PDF Tageszeitungproduktion (Datei upload)
Wir wollen auf jedenfall eine Anzeige die auch effektreich ist, nicht nur 2-dimensional und platt bleibt, sondern auch verschiedene Tiefen hat. Aber sie soll trotzdem plakativ sein.
Die Anzeige muss Seriös, Auffälig, gut lesbar, edel, frisch,..... AKTION!!
Zielgruppe ansprechen
Direkt erkennbar sein was die Anzeige bezwecken soll
Unser Hauptinteresse liegt auf den gelben ketten, davon haben wir auch 2 Bilder beigefügt.
Das wichtigste Bild ist Bild: "bernstein_2.jpg", dieses sollte schon irgendwo groß auftauchen.
Das soll auf die Anzeige:
- Textteil wie Beispielsdatei.
- AKTION
- Was....Bernstein Ankaufs-Tage in Wien
- Bernstein-Wertschätzung und Ankauf in Wien
- Wann.....vom 03.08.2017-05.08.2017
- Uhrzeit von 10:00 Uhr bis 17:00 Uhr
- Wo.... Hotel Ostara Palais, Lindauer Gasse 14, 1010 Wien, Raum: Salon 3
- Was Kaufen Wir....... Bernsteinschmuck, Bernsteinketten, Bernsteinobjekte, Rohbernsteine ab 10 g,
Bernstein Kunstgegenstände.
- Wir bieten Ihnen eine kostenlose Wertschätzung Ihrer Bernsteinstücke sowie einen
Bar-Ankauf vor Ort.
- Unser Logo
- Unsere Website www.lindwerk-handel.de
- rechts oben in der Anzeige muss das Wort -ANZEIGE- in klein stehen.
Vermerk, Achtung !!! wir kaufen nur unbehandelten Naturbernstein!!!!
siehe Bsp. Anzeige Wien bei (Datei upload)

```html
<!DOCTYPE html>
<html lang="de">
<head>
<meta charset="utf-8">
<title>Vergessene Schätze – Anzeige</title>
<link href="https://fonts.googleapis.com/css2?family=Montserrat:wght@300;400;500;600;700&display=swap" rel="stylesheet">
<style>
  :root {
    --backdrop: #e4e4e4;
    --paper: #ffffff;
    --ink: #2f2f2f;
    --body-ink: #3c3c3c;
    --brown: #7b5a3a;
    --amber: #f0a72a;
    --charcoal: #333334;
    --muted: #9a9a9a;
    --white: #ffffff;
  }
  * { box-sizing: border-box; margin: 0; padding: 0; }
  html, body {
    width: 1200px; height: 833px; overflow: hidden;
    background: var(--backdrop);
    font-family: "Montserrat", sans-serif;
  }
  .ad {
    position: absolute; left: 306px; top: 16px;
    width: 587px; height: 800px;
    background: var(--paper);
    overflow: hidden;
    box-shadow: 0 2px 10px rgba(0,0,0,.12);
  }
  .ad__label {
    position: absolute; right: 40px; top: 46px;
    font-size: 7px; letter-spacing: .08em; color: var(--muted);
  }
  .ad__title {
    position: absolute; left: 41px; top: 38px;
    font-size: 26px; font-weight: 600; color: var(--ink);
    letter-spacing: -.01em;
  }
  .hero-necklace {
    position: absolute; left: 312px; top: 40px; width: 240px; height: 122px;
    border-radius: 50% 50% 46% 46%;
    background: radial-gradient(ellipse at 55% 60%, #f7b733 0%, #e88f1c 45%, #d2771a 70%, rgba(255,255,255,0) 72%);
  }
  .ad__intro {
    position: absolute; left: 41px; top: 84px; width: 270px;
    font-size: 9.4px; line-height: 13.4px; font-weight: 600; color: var(--brown);
  }
  .article {
    position: absolute; left: 41px; top: 178px; width: 510px; height: 264px;
    column-count: 3; column-gap: 11px; column-fill: auto;
    font-size: 6.9px; line-height: 12.4px; font-weight: 300; color: var(--body-ink);
    text-align: justify; hyphens: auto; -webkit-hyphens: auto;
    word-spacing: -0.2px;
  }
  .article h3 {
    font-size: 8px; font-weight: 600; color: var(--brown);
    margin-top: 8px; line-height: 12px;
  }
  .products { position: absolute; top: 452px; left: 34px; height: 60px; }
  .product { position: absolute; }
  .product--pendant { left: 0; top: 4px; width: 96px; height: 50px; border-radius: 50%;
    background: radial-gradient(ellipse at 50% 50%, #f2c12c 0%, #d9a21c 45%, #8c8c8c 60%, rgba(255,255,255,0) 72%); }
  .product--bracelet { left: 104px; top: 0; width: 100px; height: 58px; border-radius: 40%;
    background: radial-gradient(ellipse at 50% 50%, #c7662a 0%, #a8a8a8 50%, rgba(255,255,255,0) 72%); }
  .product--rough { left: 224px; top: 10px; width: 124px; height: 44px; border-radius: 45%;
    background: radial-gradient(ellipse at 60% 55%, #eea431 0%, #b06a2a 45%, rgba(255,255,255,0) 72%); }
  .wave { position: absolute; left: 0; top: 0; width: 587px; height: 800px; }
  .portrait {
    position: absolute; left: 330px; top: 540px; width: 257px; height: 260px;
    background: linear-gradient(180deg, rgba(74,74,75,0) 0%, #3d3d3e 30%, #2c2c2d 100%);
  }
  .badge {
    position: absolute; left: 451px; top: 443px; width: 106px; height: 106px;
    border-radius: 50%; background: var(--amber);
    display: flex; align-items: center; justify-content: center;
    font-size: 17px; font-weight: 700; color: var(--charcoal);
  }
  .offer { position: absolute; left: 41px; top: 0; color: var(--white); }
  .offer__title {
    position: absolute; top: 577px; width: 230px;
    font-size: 16.5px; line-height: 22px; font-weight: 600; color: var(--amber);
  }
  .offer__lead {
    position: absolute; top: 630px; width: 260px;
    font-size: 7.8px; line-height: 12px; font-weight: 600;
  }
  .offer__heading { font-size: 8.6px; font-weight: 600; color: var(--amber); line-height: 12px; }
  .offer__text { font-size: 7.6px; line-height: 12px; font-weight: 400; }
  .offer__buy { position: absolute; top: 666px; width: 260px; }
  .info { position: absolute; display: flex; gap: 5px; }
  .info svg { width: 11px; height: 11px; flex: none; margin-top: 1px; }
  .info--date { top: 714px; left: 0; width: 130px; }
  .info--place { top: 714px; left: 124px; width: 150px; }
  .info--phone { top: 760px; left: 0; width: 130px; }
  .info--web { top: 760px; left: 124px; width: 160px; }
  .web { font-size: 8.2px; font-weight: 600; color: var(--amber); }
  .brand {
    position: absolute; left: 444px; top: 752px;
    display: flex; align-items: center; gap: 5px;
    font-size: 9.5px; font-weight: 400; letter-spacing: .06em; color: var(--white);
  }
  .brand__dot { width: 9px; height: 9px; border-radius: 50%; background: var(--amber); }
</style>
</head>
<body>
<main class="ad">
  <div class="ad__label">ANZEIGE</div>
  <h1 class="ad__title">Vergessene Schätze</h1>
  <div class="hero-necklace" role="img" aria-label="Foto: gelb-orange Bernsteinkette"></div>

  <p class="ad__intro">Einst als kostbare Fracht entlang der Bernsteinstraße (östliche römische Route) gelangte Bernstein von der Nord- und Ostsee nach Süden in den Mittelmeerraum. Gezeichnet durch kunstvoll gefertigte Gegenstände und allerlei Schmuck rühmt sich das fossile Harz einer langen und vielfältigen Geschichte.</p>

  <article class="article">
    <p>Doch diese facetten&shy;reiche Geschichte scheint heute für die meisten in Verges&shy;sen&shy;heit geraten zu sein und klingt bes&shy;ten&shy;falls noch wie ein Märchen aus der Kindheit. Oft sogar als „lang&shy;weilig“ oder „aus der Mode gekommen“ gebrand&shy;markt, wurde der Natur&shy;bernstein hier zunehmend von Juwelier-Schau&shy;fens&shy;tern und Vitrinen verbannt.</p>
    <h3>Ein neues Kapitel</h3>
    <p>Nichts&shy;desto&shy;weniger wird dem Bernstein heute weltweit mehr Wert&shy;schätzung gezollt als je zuvor. Seit Neuestem wurde ein neues Kapitel aufge&shy;schlagen. Die Bernstein&shy;straße, die einst gen Süden ging, führt heute bis nach China im Fernen Osten. Die aktuelle Nachfrage aus Asien hat den Handel mit Bernstein auf ganz neue Weise wieder&shy;belebt und den Preis teilweise beträchtlich ansteigen lassen. Was mitunter in Wiener Haus&shy;halten seit Jahr&shy;zehnten in Schmuck&shy;kästchen verstaubt, wird in China als be&shy;gehrtes Schmuck&shy;stück teuer gehandelt. Dort gilt Bernstein unter anderem als Symbol des Reichtums und wird stolz in der Öffent&shy;lich&shy;keit getragen.</p>
    <h3>Große Werte</h3>
    <p>Die Wert&shy;bestimmung für Bernstein hat sich jedoch gewandelt und abhängig von bestimmten Merkmalen variiert der Preis sehr stark. Der hier sonst sehr übliche cognac&shy;farbene und transpa&shy;rente Bernstein&shy;schmuck ist kaum mehr gefragt und in jeglicher Form behan&shy;delter oder gepresster Bernstein findet so gut wie keine Beachtung mehr. Dahin&shy;gegen dominiert heute vor allem der unbehan&shy;delte natur&shy;belassene Honig&shy;bernstein den Handel. Gelb bis orange&shy;farbene milchige in Oliven- oder Kugelform gefertigte Ketten sind die absoluten Renner. Antike Bernstein&shy;ketten, die durch Verwit&shy;terung im Laufe der Jahre unter&shy;schiedlich stark rot bis rotbraun gefärbt wurden, sind besonders interessant. Auch sonstige Schmuck&shy;stücke, wie etwa Armbänder, Anhänger, Ringe, Broschen und andere Klein&shy;gegen&shy;stände sind beliebt. Das gilt auch für Schmuck&shy;scha&shy;tullen, Schnitze&shy;reien und Kunst&shy;gegen&shy;stände aus Natur-Bernstein. Zum einen ist natürlich das Alter und der Zustand für den Preis entscheidend, aber auch Dinge wie Farbe, Größe und Marmo&shy;rierung sind wichtige Faktoren. Sammler bevor&shy;zugen überwiegend gut erhaltene und antike Stücke. Es empfiehlt sich in jedem Fall einen geeigneten Fachmann zu Rate zu ziehen.</p>
  </article>

  <div class="products">
    <div class="product product--pendant" role="img" aria-label="Foto: Bernsteinanhänger in Silberfassung"></div>
    <div class="product product--bracelet" role="img" aria-label="Foto: Silberarmband mit Bernsteingliedern"></div>
    <div class="product product--rough" role="img" aria-label="Foto: Rohbernsteinstücke"></div>
  </div>

  <svg class="wave" viewBox="0 0 587 800" aria-hidden="true">
    <path d="M0 546 Q300 532 587 446 L587 800 L0 800 Z" fill="var(--amber)"/>
    <path d="M0 556 Q320 548 587 478 L587 800 L0 800 Z" fill="var(--charcoal)"/>
  </svg>

  <div class="portrait" role="img" aria-label="Foto: Fachfrau prüft Bernstein mit einer Lupe"></div>

  <div class="badge">AKTION</div>

  <section class="offer">
    <h2 class="offer__title">Bernstein-Wertschätzung und Ankauf in Wien</h2>
    <p class="offer__lead">Wir bieten Ihnen eine kostenlose Wertschätzung Ihrer Bernsteinstücke sowie einen Bar-Ankauf vor Ort.</p>
    <div class="offer__buy">
      <p class="offer__heading">Wir kaufen</p>
      <p class="offer__text">Bernsteinschmuck, Bernsteinketten, Rohbernsteine<br>ab 10 g und Kunstgegenstände aus Bernstein.</p>
    </div>

    <div class="info info--date">
      <svg viewBox="0 0 12 12"><rect x="1" y="2" width="10" height="9" rx="1" fill="none" stroke="var(--amber)" stroke-width="1.2"/><rect x="1" y="2" width="10" height="2.5" fill="var(--amber)"/><rect x="3" y="0.5" width="1.2" height="2.5" fill="var(--amber)"/><rect x="7.8" y="0.5" width="1.2" height="2.5" fill="var(--amber)"/><rect x="3" y="6" width="1.5" height="1.5" fill="var(--amber)"/><rect x="5.3" y="6" width="1.5" height="1.5" fill="var(--amber)"/><rect x="7.6" y="6" width="1.5" height="1.5" fill="var(--amber)"/></svg>
      <div>
        <p class="offer__heading">Termin</p>
        <p class="offer__text">03. bis 05.08.2017<br>10:00 bis 17:00 Uhr</p>
      </div>
    </div>

    <div class="info info--place">
      <svg viewBox="0 0 12 12"><path d="M6 0.5 C3.3 0.5 1.8 2.5 1.8 4.5 C1.8 7.3 6 11.5 6 11.5 C6 11.5 10.2 7.3 10.2 4.5 C10.2 2.5 8.7 0.5 6 0.5 Z" fill="var(--amber)"/><circle cx="6" cy="4.6" r="1.6" fill="var(--charcoal)"/></svg>
      <div>
        <p class="offer__heading">Hotel Ostara Palais</p>
        <p class="offer__text">Lindauer Gasse 14, 1010 Wien<br>Raum: Salon 3</p>
      </div>
    </div>

    <div class="info info--phone">
      <svg viewBox="0 0 12 12"><path d="M2.5 1 L4.5 1 L5.3 3.6 L4 4.6 C4.7 6.1 5.9 7.3 7.4 8 L8.4 6.7 L11 7.5 L11 9.5 C11 10.4 10.3 11 9.4 11 C5 10.7 1.3 7 1 2.6 C1 1.7 1.6 1 2.5 1 Z" fill="var(--amber)"/></svg>
      <p class="offer__text">+43 660 5128 3307</p>
    </div>

    <div class="info info--web">
      <p class="web">www.lindwerk-handel.de</p>
    </div>
  </section>

  <div class="brand"><span class="brand__dot"></span>LINDWERK HANDEL</div>
</main>
</body>
</html>
```